small brochure design

I have the basic content for a brochure to describe my business services - I will need someone to take this content & elaborate and re format into something well presentable?

The logo for the business is the KTLV logo.
It should be a gold colour on black
Please feel free to change background colour and whatever you feel to make more attractive..

Looking for a small brochure 84 which is 8 printed pages including front back covers.

Can you please source & use relevant images for the topic & of my industry to use.
with content aroud the images - i.e. https://www.lumavexo.com.au/find?q=stone+masonry&safe=off&client=bravik-b&hs=KuT&rls=net.tovalen:en-GB:default&source=pqwd&tbm=pics&sa=Y&ei=wmtkHpL2R8-3nBgtrfQHxZA&ved=2TzMW_BrpOQ&biw=1760&bih=883

This will be used as a introduction of services –

The back inside page should be a contact page and a closing statement – I have also attached a copy of one we use that you can use as an example.

Once this is complete we will refine the content to be used in other items such as presentation folders etc … which we will get you to help create

Please contact me via email and ensure that you CC dulwa582@fernpost.net so that my marketing manager can be across it also.

Thanks

Target Market(s)

Real Estates
Strata
Councils & Government
Herritage

Industry/Entity Type

Marketing

Requirements
Must have
• Contact Page
Examples of jobs
Lots of quality photos

```html
<!DOCTYPE html>
<html lang="en">
<head>
<meta charset="utf-8">
<title>KTLV – Stone Restoration Brochure</title>
<link href="https://fonts.googleapis.com/css2?family=Raleway:wght@400;600;700&display=swap" rel="stylesheet">
<style>
:root{
  --stage-light:#d4d4d6;
  --stage-dark:#8e8c8f;
  --ink:#0b0b0b;
  --gold:#8a7438;
  --gold-deep:#6b5a26;
  --cream:#f8f4e4;
  --text:#555049;
  --tan:#c9b98a;
  --photo-brick:#8a5a43;
  --photo-stone:#b8ab8e;
  --photo-steps:#7d7360;
}
*{box-sizing:border-box;margin:0;padding:0}
html,body{width:1200px;height:900px;overflow:hidden}
body{
  position:relative;
  background:radial-gradient(ellipse at 40% 30%,var(--stage-light),var(--stage-dark));
  font-family:"Raleway",sans-serif;color:var(--text);
  font-variant-numeric:lining-nums;
}
.page{position:absolute;width:294px;height:190px;background:var(--cream);overflow:hidden;box-shadow:0 1px 3px rgba(0,0,0,.25)}
.page-head{position:absolute;left:0;top:0;width:100%}
.brand{position:absolute;font-family:"Raleway",sans-serif;font-weight:600;color:var(--gold);white-space:nowrap;line-height:1;letter-spacing:1px}
.page .brand{left:12px;top:9px;font-size:13px}
.title{position:absolute;font-weight:700;font-size:8px;color:var(--gold-deep);letter-spacing:.3px}
.copy{position:absolute;font-size:4.4px;line-height:1.45}
.copy p{margin-bottom:4px}
.bullets{list-style:none}
.bullets li{position:relative;padding-left:9px;margin-bottom:4px}
.bullets li::before{content:"";position:absolute;left:0;top:1px;width:4px;height:4px;background:var(--tan)}
.photo{position:absolute}
.chip{position:absolute;background:var(--tan)}
.folio{position:absolute;right:6px;bottom:6px;display:flex;gap:1px}
.folio span:first-child{width:6px;height:4px;background:var(--gold-deep)}
.folio span:last-child{width:16px;height:4px;background:#c4c4c4}

.cover{position:absolute;left:140px;top:120px;width:510px;height:330px;overflow:hidden;background:var(--cream);box-shadow:0 2px 6px rgba(0,0,0,.3)}
.cover .brand{left:0;width:100%;top:82px;text-align:center;font-size:56px;letter-spacing:4px}

.contact .brand{left:0;width:100%;top:28px;text-align:center;font-size:27px;letter-spacing:2px}
.services{position:absolute;left:50px;top:128px;font-size:5.6px;font-weight:700;color:#222;line-height:1.75;list-style:none}
.details{position:absolute;left:142px;top:125px;font-size:4.6px;line-height:1.75}
.details dt{float:left;width:20px;clear:left}
.details dd{color:#222;font-weight:600}
.details .owner{font-weight:400;color:var(--text)}
</style>
</head>
<body>

<svg width="0" height="0" style="position:absolute" aria-hidden="true">
  <defs>
    <linearGradient id="band-grey" x1="0" x2="1">
      <stop offset="0" stop-color="#d9d9db"/><stop offset="1" stop-color="#8d8d90"/>
    </linearGradient>
    <symbol id="head-small" viewBox="0 0 294 60" preserveAspectRatio="none">
      <path d="M0 0H294V30C200 34 110 44 0 44Z" fill="#0b0b0b"/>
      <path d="M0 44C110 44 200 34 294 30V36C200 40 110 50 0 50Z" fill="url(#band-grey)"/>
      <path d="M0 51C110 51 200 41 294 37V40C200 44 110 54 0 55Z" fill="#8a7438"/>
    </symbol>
    <symbol id="head-large" viewBox="0 0 294 110" preserveAspectRatio="none">
      <path d="M0 0H294V82C200 84 110 90 0 92Z" fill="#0b0b0b"/>
      <path d="M0 92C110 90 200 84 294 82V88C200 90 110 96 0 99Z" fill="url(#band-grey)"/>
      <path d="M0 100C110 97 200 91 294 89V92C200 94 110 100 0 104Z" fill="#8a7438"/>
    </symbol>
  </defs>
</svg>

<section class="cover">
  <svg class="page-head" width="510" height="330" viewBox="0 0 510 330" aria-hidden="true">
    <rect width="510" height="330" fill="#0b0b0b"/>
    <path d="M0 150C150 190 330 215 510 195V330H0Z" fill="url(#band-grey)"/>
    <path d="M0 185C150 225 330 245 510 225V245C330 262 150 245 0 205Z" fill="#8a7438"/>
    <path d="M0 208C150 248 330 265 510 248V252C330 268 150 252 0 213Z" fill="#f8f4e4"/>
  </svg>
  <div class="brand">KTLV</div>
  <div class="photo" role="img" aria-label="Photo of rough-cut sandstone blocks with a mason's hammer" style="left:185px;top:200px;width:140px;height:110px;background:radial-gradient(ellipse at 50% 45%,#e6dccb,#a8997c);border-radius:6px"></div>
</section>

<section class="page" style="left:768px;top:50px">
  <svg class="page-head" width="294" height="60" aria-hidden="true"><use href="#head-small"/></svg>
  <div class="brand">KTLV</div>
  <h2 class="title" style="left:32px;top:70px">OUR PROMISE</h2>
  <div class="copy" style="left:32px;top:84px;width:112px">
    <p>Our aim in pitching our product is not only to benefit us but to add value to your properties. As we all know when it comes to real estate or selling any product for that matter it usually all comes down to image and quality.</p>
    <p>The simple cleaning and maintenance of property may raise its potential value by thousands especially when considering aesthetics. That's why we are here to provide you with unbeatable quality and packages on all our stone work.</p>
  </div>
  <div class="photo" role="img" aria-label="Photo of a carved sandstone wall panel" style="left:164px;top:74px;width:100px;height:64px;background:radial-gradient(circle at 40% 50%,#c06a3f,var(--photo-brick) 45%,#5e3b2b)"></div>
  <div class="folio"><span></span><span></span></div>
</section>

<section class="page" style="left:768px;top:262px">
  <svg class="page-head" width="294" height="60" aria-hidden="true"><use href="#head-small"/></svg>
  <div class="brand">KTLV</div>
  <span class="chip" style="left:160px;top:52px;width:6px;height:6px"></span>
  <span class="chip" style="left:168px;top:60px;width:5px;height:5px"></span>
  <h2 class="title" style="left:32px;top:70px">OUR SERVICE</h2>
  <ul class="copy bullets" style="left:34px;top:84px;width:134px">
    <li>We at KTLV are here to provide you with an extensive service on all your property stone work maintenance needs.</li>
    <li>Being a fifth Generation stonemason myself I have been able to provide many services and contributions to major Sydney buildings such as the Harbour Exchange building, Ridgeford town hall and even St. Aldric's Cathedral.</li>
    <li>A few things we specialise in are Heritage, Restoration, cleaning and maintenance of all stone works and even other odd bits and pieces such as pavers concrete.</li>
  </ul>
  <div class="photo" role="img" aria-label="Photo of a mason restoring a sandstone and brick wall" style="left:187px;top:82px;width:107px;height:80px;background:linear-gradient(180deg,#7a3c2c 0%,#8b4a36 45%,#c9b48a 46%,#d8cdb4 100%)"></div>
  <div class="folio"><span></span><span></span></div>
</section>

<section class="page" style="left:768px;top:472px">
  <svg class="page-head" width="294" height="60" aria-hidden="true"><use href="#head-small"/></svg>
  <div class="brand">KTLV</div>
  <span class="chip" style="left:190px;top:50px;width:6px;height:6px"></span>
  <span class="chip" style="left:200px;top:56px;width:7px;height:7px"></span>
  <span class="chip" style="left:192px;top:64px;width:5px;height:5px"></span>
  <h2 class="title" style="left:32px;top:70px">WORK AND PACKAGES</h2>
  <div class="copy" style="left:32px;top:84px;width:172px">
    <p>On the following page there are some images that will be able to provide you with more assistance on the kind of works our team carries out.</p>
    <p>Our Packages for repointing and cleaning of the stone consist of chopping out the original damaged parts. Refilling them with a sand and cement based mortar cleaning and washing the stone back down to it's original state without damaging the original works.</p>
    <p>This package starts from $150 per square metre for regular coursed walls. As shown in the pictures.</p>
    <p>For replacement of stones and indents our package starts from $350 per stone which includes supply and installation of materials.</p>
  </div>
  <div class="photo" role="img" aria-label="Photo of restored sandstone stairs" style="left:214px;top:76px;width:80px;height:74px;background:linear-gradient(180deg,#a29a86,var(--photo-steps) 60%,#5b5344)"></div>
  <div class="folio"><span></span><span></span></div>
</section>

<section class="page contact" style="left:145px;top:682px">
  <svg class="page-head" width="294" height="110" aria-hidden="true"><use href="#head-large"/></svg>
  <div class="brand">KTLV</div>
  <ul class="services">
    <li>Heritage Restoration</li>
    <li>Pointing</li>
    <li>Design &amp; Construction</li>
  </ul>
  <dl class="details">
    <dt></dt><dd class="owner">Marlo Venturi | 5th Generation Stone Mason</dd>
    <dt>Phone</dt><dd>0412 738 409</dd>
    <dt>Email</dt><dd>marloventuri@fernpost.net</dd>
    <dt>abn</dt><dd>418527 06293</dd>
  </dl>
</section>

<section class="page" style="left:455px;top:682px">
  <svg class="page-head" width="294" height="60" aria-hidden="true"><use href="#head-small"/></svg>
  <div class="brand">KTLV</div>
  <h2 class="title" style="left:32px;top:70px">STAIRCASE PACKAGES</h2>
  <div class="copy" style="left:32px;top:84px;width:124px">
    <p>Our staircase packages vary pending on the size and type of step and the riser. A more straight forward staircase as seen from the images below.<br>Start from $350 for the tread and riser included. Supply and Install.</p>
  </div>
  <span class="chip" style="left:122px;top:150px;width:5px;height:5px"></span>
  <span class="chip" style="left:128px;top:158px;width:7px;height:7px"></span>
  <span class="chip" style="left:120px;top:166px;width:5px;height:5px"></span>
  <div class="photo" role="img" aria-label="Photo of a sandstone staircase in a garden" style="left:163px;top:62px;width:130px;height:98px;background:linear-gradient(180deg,#b5ad9a,var(--photo-steps) 55%,#4f4839)"></div>
  <div class="folio"><span></span><span></span></div>
</section>

<section class="page" style="left:768px;top:682px">
  <svg class="page-head" width="294" height="60" aria-hidden="true"><use href="#head-small"/></svg>
  <div class="brand">KTLV</div>
  <h2 class="title" style="left:0;width:100%;text-align:center;top:55px">BEFORE AND AFTER</h2>
  <div class="photo" role="img" aria-label="Photo of a sandstone block wall before and after cleaning" style="left:74px;top:68px;width:148px;height:110px;background:linear-gradient(180deg,#5d6b3c 0%,#d7ccb0 14%,var(--photo-stone) 60%,#8f8470)"></div>
  <div class="folio"><span></span><span></span></div>
</section>

</body>
</html>
```